2367 Halvorsen Avenue Medical Centre

We are looking for a design for new medical clinic.
We are accepting new patients at this new medical centre grand opening. Walk-ins are welcome.
Our cardiac and vascular surgical specialists are department heads at St Alder's Hospital, a leading teaching hospital in Toronto. These specialists will see cardiovascular consults are well as pre-surgical and post-surgical consultations and follow-ups.
Our lab is affiliated with several nuclear medicine clinics in the GTA.
Our Services Includes:
Family Practice
Cardiology Diagnostics
Cardiac & Vascular Surgical Consultation
Ultrasound & Vascular Testing
Open 6 days a week.
Ample Free Parking
Friendly Staffs

Target Market(s)

New Patients. Families of any age. Ethnic groups including Asians & Africans.

Industry/Entity Type

Medical

Font styles to use
Serif
Sans Serif
Decorative
Script
Other font styles liked:
• Arial calibri, verdana

Requirements
Must have
• Address:
• 2367 Halvorsen Avenue East
• Unit 225
• Scarborough, Ontario
• K7T 2P4
• Tel: (416) 555-0148
Nice to have
• Caring and inviting environment.
• Simple but classy.
• Standout colors.
Should not have
• Busy images. Aside from this, any ideas are welcome.

```html
<!DOCTYPE html>
<html lang="en">
<head>
<meta charset="utf-8">
<title>New Medical Clinic Flyer</title>
<link rel="stylesheet" href="https://fonts.googleapis.com/css2?family=Montserrat:wght@500;700&family=Oswald:wght@500;700&family=Lato:wght@400;700&display=swap">
<style>
  :root{
    --stage:#2aa7e0;
    --teal:#0d5e7a;
    --teal-dark:#0a4d66;
    --lime:#d3f2a4;
    --lime-text:#c8ef8f;
    --green:#6b9a1f;
    --blue:#0d62c4;
    --navy:#0b3d7a;
    --ink:#163a5c;
    --text:#2c2c2c;
    --white:#ffffff;
  }
  *{margin:0;padding:0;box-sizing:border-box}
  html,body{width:1200px;height:912px;overflow:hidden;background:var(--stage)}
  .flyer{position:absolute;left:280px;top:26px;width:640px;height:860px;background:var(--white);overflow:hidden;box-shadow:0 6px 24px rgba(0,0,0,.25)}
  .flyer__art{position:absolute;inset:0}
  .title{position:absolute;right:40px;top:32px;text-align:right;font-family:"Montserrat",sans-serif;color:var(--blue);line-height:1}
  .title__small{font-size:28px;font-weight:500;letter-spacing:1px}
  .title__big{font-size:56px;font-weight:700;letter-spacing:2px;margin-top:4px}
  .booking{position:absolute;left:360px;top:256px;line-height:1.02}
  .booking__lead{font-family:"Oswald",sans-serif;font-weight:700;font-size:30px;color:var(--blue)}
  .booking__main{font-family:"Oswald",sans-serif;font-weight:500;font-size:44px;color:var(--navy);letter-spacing:-.5px}
  .booking__call{font-family:"Montserrat",sans-serif;font-weight:500;font-size:30px;color:var(--white);margin-top:4px}
  .booking__phone{font-family:"Oswald",sans-serif;font-weight:700;font-size:36px;color:var(--ink);margin-top:2px}
  .badge{position:absolute;left:40px;top:400px;width:260px;height:260px;display:flex;align-items:center;justify-content:center;text-align:center;font-family:"Montserrat",sans-serif;font-weight:700;color:var(--white);font-size:32px;line-height:1.08;letter-spacing:1px}
  .badge svg{position:absolute;inset:0}
  .badge__text{position:relative}
  .services{position:absolute;right:36px;top:462px;text-align:right}
  .services__heading{font-family:"Oswald",sans-serif;font-weight:500;font-size:22px;color:var(--green);margin-bottom:4px}
  .services__list{list-style:none;font-family:"Lato",sans-serif;font-size:15px;color:var(--text);line-height:1.6}
  .services__list li::after{content:"";display:inline-block;width:6px;height:6px;border-radius:50%;background:var(--green);margin-left:8px;vertical-align:middle}
  .cta{position:absolute;right:36px;top:684px;text-align:left;font-family:"Montserrat",sans-serif;font-weight:700;color:var(--white);font-size:26px;line-height:1.15}
  .cta__phone{font-weight:500}
  .address{position:absolute;left:36px;top:778px;font-family:"Lato",sans-serif;color:var(--white);font-size:17px;line-height:1.35}
  .address__label{font-family:"Montserrat",sans-serif;font-weight:500;font-size:22px;color:var(--lime-text)}
</style>
</head>
<body>
<main class="flyer">
  <svg class="flyer__art" width="640" height="860" viewBox="0 0 640 860">
    <defs>
      <linearGradient id="photoTone" x1="0" y1="1" x2="1" y2="0">
        <stop offset="0" stop-color="#c9d3cf"/>
        <stop offset=".55" stop-color="#e6ebea"/>
        <stop offset="1" stop-color="#f7f8f8"/>
      </linearGradient>
      <linearGradient id="skyBand" x1="0" y1="0" x2="1" y2="1">
        <stop offset="0" stop-color="#6fd6fb"/>
        <stop offset="1" stop-color="#b9ecfd"/>
      </linearGradient>
      <linearGradient id="paleBand" x1="0" y1="1" x2="1" y2="0">
        <stop offset="0" stop-color="#e8e8e8"/>
        <stop offset="1" stop-color="#ffffff"/>
      </linearGradient>
    </defs>
    <polygon points="0,0 640,0 640,120 0,360" fill="url(#photoTone)" role="img" aria-label="Photograph of smiling clinic staff in white coats in front of pharmacy shelves"/>
    <polygon points="0,360 640,120 640,133 0,373" fill="var(--lime)"/>
    <polygon points="0,373 640,133 640,156 0,396" fill="var(--teal)"/>
    <polygon points="0,396 640,156 640,400 0,660" fill="url(#skyBand)"/>
    <polygon points="0,660 640,400 640,412 0,672" fill="var(--teal)"/>
    <polygon points="0,672 640,412 640,422 0,682" fill="var(--lime)"/>
    <polygon points="0,682 640,422 640,620 0,760" fill="url(#paleBand)"/>
    <polygon points="0,760 640,620 640,628 0,768" fill="var(--lime)"/>
    <polygon points="0,768 640,628 640,860 0,860" fill="var(--teal)"/>
  </svg>

  <header class="title">
    <div class="title__small">NEW MEDICAL</div>
    <div class="title__big">CLINIC</div>
  </header>

  <section class="badge">
    <svg width="260" height="260" viewBox="-130 -130 260 260" aria-hidden="true">
      <g fill="var(--white)">
        <rect x="-92" y="-92" width="184" height="184"/>
        <rect x="-92" y="-92" width="184" height="184" transform="rotate(15)"/>
        <rect x="-92" y="-92" width="184" height="184" transform="rotate(30)"/>
        <rect x="-92" y="-92" width="184" height="184" transform="rotate(45)"/>
        <rect x="-92" y="-92" width="184" height="184" transform="rotate(60)"/>
        <rect x="-92" y="-92" width="184" height="184" transform="rotate(75)"/>
      </g>
      <g fill="var(--teal-dark)">
        <rect x="-86" y="-86" width="172" height="172"/>
        <rect x="-86" y="-86" width="172" height="172" transform="rotate(15)"/>
        <rect x="-86" y="-86" width="172" height="172" transform="rotate(30)"/>
        <rect x="-86" y="-86" width="172" height="172" transform="rotate(45)"/>
        <rect x="-86" y="-86" width="172" height="172" transform="rotate(60)"/>
        <rect x="-86" y="-86" width="172" height="172" transform="rotate(75)"/>
      </g>
      <circle r="92" fill="#1a7a9a" opacity=".45"/>
    </svg>
    <div class="badge__text">OPEN<br>6 DAYS<br>A WEEK</div>
  </section>

  <section class="booking">
    <div class="booking__lead">TO BOOK</div>
    <div class="booking__main">APPOINTMENT</div>
    <div class="booking__call">PLEASE CALL</div>
    <div class="booking__phone">(416) 555-0148</div>
  </section>

  <section class="services">
    <h2 class="services__heading">SERVICES INCLUDES:</h2>
    <ul class="services__list">
      <li>Family Practice</li>
      <li>Cardiology Diagnostics</li>
      <li>Cardiac &amp; Vascular Surgical Consultation</li>
      <li>Ultrasound &amp; Vascular</li>
    </ul>
  </section>

  <section class="cta">
    <div>CALL US NOW:</div>
    <div class="cta__phone">(416) 555-0148</div>
  </section>

  <footer class="address">
    <div class="address__label">ADDRESS:</div>
    <div>2367 Halvorsen Avenue East Unit 225</div>
    <div>Scarborough, Ontario K7T 2P4</div>
  </footer>
</main>
</body>
</html>
```